Velmont Recycling needs a new web design

We need a new web design for our company based in Austin, TX. We resell and recycling electronics such as laptops, computer components, Zelvos, Quorbs, etc. Since our inception over ten years ago, we’ve become one of the premier electronics recycling and remarketing companies in Austin, Texas.

```html
<!DOCTYPE html>
<html lang="en">
<head>
<meta charset="utf-8">
<title>Velmont Recycling — Computer Recycling Made Easy</title>
<link href="https://fonts.googleapis.com/css2?family=Raleway:wght@300;400;600;700;800&family=Roboto:wght@300;400;500&display=swap" rel="stylesheet">
<style>
  :root {
    --blue: #1275c0;
    --blue-deep: #0e5f9f;
    --sky: #2aa9e8;
    --ink: #1f1f1f;
    --muted: #9a9a9a;
    --bar: #2a2a2a;
    --white: #ffffff;
    --wood-dark: #3b2419;
    --wood-mid: #6b4634;
  }
  * { box-sizing: border-box; margin: 0; padding: 0; }
  html, body { width: 1200px; height: 1000px; overflow: hidden; background: var(--white); }
  body { position: relative; font-family: "Roboto", sans-serif; }

  .header-band {
    position: absolute; left: 0; top: 0; width: 1200px; height: 96px;
    background: linear-gradient(90deg, #1673b8 0%, #1e84cc 45%, #1470b6 100%);
  }
  .brand-card {
    position: absolute; left: 186px; top: 0; width: 263px; height: 104px;
    background: var(--white); border-radius: 0 0 4px 4px;
    box-shadow: 0 4px 12px rgba(0,0,0,.25);
    display: flex; align-items: center; justify-content: center; gap: 10px;
  }
  .brand-dot { width: 26px; height: 26px; border-radius: 50%; background: var(--blue); }
  .brand-name {
    font-family: "Raleway", sans-serif; font-weight: 800; font-size: 21px; color: var(--blue);
  }
  .contact-bar {
    position: absolute; left: 565px; top: 0; width: 460px; height: 29px;
    background: var(--bar); border-radius: 0 0 4px 4px;
    display: flex; align-items: center; font-size: 11px; color: #d8d8d8;
  }
  .contact-item { display: flex; align-items: center; gap: 8px; }
  .contact-mail { position: absolute; left: 36px; }
  .contact-phone { position: absolute; left: 227px; }
  .divider { position: absolute; top: 7px; width: 1px; height: 15px; background: #555; transform: skewX(-15deg); }
  .social { position: absolute; left: 376px; display: flex; gap: 21px; }
  .social span { width: 7px; height: 7px; border-radius: 50%; background: var(--white); display: block; }

  .main-nav { position: absolute; top: 57px; left: 628px; font-family: "Raleway", sans-serif; font-weight: 700; font-size: 10px; color: var(--white); }
  .main-nav a { position: absolute; color: inherit; text-decoration: none; white-space: nowrap; }
  .nav-cta {
    position: absolute; left: 895px; top: 48px; width: 130px; height: 29px;
    background: var(--sky); border-radius: 15px; color: var(--white);
    font-family: "Raleway", sans-serif; font-weight: 700; font-size: 10px;
    display: flex; align-items: center; justify-content: center;
  }

  .hero-photo {
    position: absolute; left: 0; top: 96px; width: 1200px; height: 521px;
    background:
      radial-gradient(ellipse at 50% 40%, #8a5d45 0%, var(--wood-mid) 40%, var(--wood-dark) 100%);
  }
  .hero-kicker {
    position: absolute; left: 0; width: 1210px; top: 177px; text-align: center;
    font-family: "Raleway", sans-serif; font-weight: 300; font-size: 36px; color: var(--white); letter-spacing: .5px;
  }
  .hero-title {
    position: absolute; left: 0; width: 1210px; top: 206px; text-align: center;
    font-family: "Raleway", sans-serif; font-weight: 300; font-size: 72px; color: var(--white); line-height: 1;
  }
  .hero-ribbon {
    position: absolute; left: 392px; top: 296px; width: 426px; height: 32px;
    background: var(--blue); color: var(--white);
    font-family: "Raleway", sans-serif; font-weight: 700; font-size: 17px;
    display: flex; align-items: center; justify-content: center;
  }
  .hero-copy {
    position: absolute; left: 405px; top: 345px; width: 400px; text-align: center;
    font-weight: 300; font-size: 13.5px; line-height: 19.5px; color: #eee;
  }
  .btn {
    position: absolute; height: 32px; display: flex; align-items: center; justify-content: center;
    font-family: "Raleway", sans-serif; font-weight: 700; font-size: 10.5px; letter-spacing: .2px;
  }
  .btn-solid { left: 492px; top: 424px; width: 98px; background: var(--blue); color: var(--white); }
  .btn-ghost { left: 612px; top: 424px; width: 141px; border: 2px solid var(--white); color: var(--white); }

  .service {
    position: absolute; top: 517px; width: 174px; height: 174px; border-radius: 50%;
    background: var(--blue); color: var(--white);
    font-family: "Raleway", sans-serif; font-weight: 700; font-size: 14px;
  }
  .service svg { position: absolute; left: 50%; top: 30px; transform: translateX(-50%); }
  .service-label { position: absolute; left: 0; width: 100%; top: 117px; text-align: center; }
  .service-logistics { left: 188px; box-shadow: 0 10px 18px rgba(0,0,0,.3); }
  .service-recycling { left: 406px; }
  .service-return { left: 619px; }
  .service-certificates { left: 839px; }

  .about-title {
    position: absolute; left: 0; width: 1200px; top: 747px; text-align: center;
    font-family: "Raleway", sans-serif; font-weight: 700; font-size: 27px; color: var(--ink);
  }
  .about-copy {
    position: absolute; left: 258px; top: 800px; width: 684px; text-align: center;
    font-weight: 300; font-size: 13.5px; line-height: 19px; color: var(--muted);
  }
  .btn-outline { left: 527px; top: 907px; width: 148px; height: 39px; border: 2px solid var(--blue-deep); color: var(--ink); }
</style>
</head>
<body>
  <header>
    <div class="header-band" role="img" aria-label="Blue-toned close-up of circuit boards"></div>
    <div class="brand-card"><span class="brand-dot"></span><span class="brand-name">Velmont Recycling</span></div>
    <div class="contact-bar">
      <div class="contact-item contact-mail">
        <svg width="11" height="11" viewBox="0 0 12 12" fill="none" stroke="#2aa9e8" stroke-width="1.2"><circle cx="6" cy="6" r="2.2"/><path d="M8.2 6v1a1.5 1.5 0 0 0 3 0V6A5.2 5.2 0 1 0 9 10.2"/></svg>
        nora@velmontrecycling.com
      </div>
      <span class="divider" style="left:200px"></span>
      <div class="contact-item contact-phone">
        <svg width="11" height="11" viewBox="0 0 12 12" fill="none" stroke="#2aa9e8" stroke-width="1.2"><path d="M2 1.5h2.2l1 2.6-1.3.9a6 6 0 0 0 3.1 3.1l.9-1.3 2.6 1V10a1 1 0 0 1-1 1A9 9 0 0 1 1 3 1 1 0 0 1 2 1.5z"/></svg>
        (512) 555-0147
      </div>
      <span class="divider" style="left:350px"></span>
      <div class="social" aria-label="Social links"><span></span><span></span><span></span></div>
    </div>
    <nav class="main-nav">
      <a style="left:0">HOME</a>
      <a style="left:52px">ABOUT</a>
      <a style="left:112px">SERVICES</a>
      <a style="left:184px">CONTACT US</a>
    </nav>
    <a class="nav-cta">SCHEDULE A PICKUP</a>
  </header>

  <section class="hero">
    <div class="hero-photo" role="img" aria-label="Computer parts, a processor, drives and a power supply laid out on a dark wooden desk"></div>
    <div class="hero-kicker">COMPUTER RECYCLING</div>
    <h1 class="hero-title">MADE EASY</h1>
    <div class="hero-ribbon">MAKE A DIFFERENCE TO OUR ENVIRONMENT</div>
    <p class="hero-copy">Want to make a difference to our environment and planet? Velmont Recycling is here to help! Velmont recycling has been helping keep the environment healthy since 2006, we specialize in recycling ...</p>
    <a class="btn btn-solid">READ MORE</a>
    <a class="btn btn-ghost">SCHEDULE A PICKUP</a>
  </section>

  <section class="services">
    <div class="service service-logistics">
      <svg width="70" height="66" viewBox="0 0 70 66" fill="none" stroke="#fff" stroke-width="2">
        <rect x="18" y="2" width="14" height="12"/><rect x="6" y="16" width="14" height="14"/><rect x="22" y="16" width="14" height="14"/>
        <rect x="2" y="32" width="38" height="20"/><path d="M40 36h14l10 10v6H40z"/><path d="M46 38v8h14"/>
        <circle cx="10" cy="58" r="4"/><circle cx="24" cy="58" r="4"/><circle cx="52" cy="58" r="4"/>
      </svg>
      <div class="service-label">LOGISTICS</div>
    </div>
    <div class="service service-recycling">
      <svg width="76" height="66" viewBox="0 0 76 66" fill="none" stroke="#fff" stroke-width="2" stroke-linejoin="round">
        <path d="M30 6 20 24l8 4 8-14 6 10-5 3h14l6-12-5 2-7-12z"/>
        <path d="M62 30l-10 6 7 13H44v-6l-8 10 8 10v-6h18l8-12z"/>
        <path d="M14 30 4 48l8 14h18V50H18l6-10 5 3-6-13z"/>
      </svg>
      <div class="service-label">RECYCLING</div>
    </div>
    <div class="service service-return">
      <svg width="76" height="66" viewBox="0 0 76 66" fill="none" stroke="#fff" stroke-width="2">
        <rect x="24" y="4" width="20" height="14"/><rect x="2" y="20" width="44" height="34"/><path d="M18 20v10h12V20"/>
        <circle cx="58" cy="50" r="14" fill="#1275c0"/><path d="M51 47a8 8 0 0 1 13-2l2-3v6h-6l2-2"/><path d="M65 53a8 8 0 0 1-13 2l-2 3v-6h6l-2 2"/>
      </svg>
      <div class="service-label">RETURN</div>
    </div>
    <div class="service service-certificates">
      <svg width="74" height="68" viewBox="0 0 74 68" fill="none" stroke="#fff" stroke-width="2">
        <path d="M40 56H2V2h70v54h-8"/><rect x="12" y="12" width="18" height="12"/><path d="M38 14h24M38 22h24M12 34h50M12 42h24"/>
        <circle cx="52" cy="48" r="8"/><path d="M47 55l-3 11 8-4 8 4-3-11"/>
      </svg>
      <div class="service-label">CERTIFICATES</div>
    </div>
  </section>

  <section class="about">
    <h2 class="about-title">About us</h2>
    <p class="about-copy">At Velmont Recycling, we're committed to providing environmentally friendly recycling solutions to Austin and the surrounding areas. Founded in 2006, our mission is to process your materials in a safe, non-hazardous manner — with an aim to keep the world environmentally clean. As a certified recycling center, we believe in promoting smart recycling habits in order to achieve long lasting results.</p>
    <a class="btn btn-outline">SCHEDULE A PICKUP</a>
  </section>
</body>
</html>
```